all sorted property services

Target Market(s)

General letter head for emails and letter quotes ect

Colors
0054AA
0677BA
7BADD7
CADEEF
E8F1F8
0094D4
00A9DD
6FCCEA
C7EBF8
E9F6FB

Requirements
Must have
• logo phone email website names
Nice to have
• what we do (from the website)

```html
<!DOCTYPE html>
<html lang="en">
<head>
<meta charset="utf-8">
<title>All Sorted Property Services – Letterhead</title>
<link rel="stylesheet" href="https://fonts.googleapis.com/css2?family=Arimo:wght@400;600&family=Open+Sans:wght@400;600&display=swap">
<style>
  :root {
    --backdrop: #ececec;
    --paper: #f6f4f5;
    --brand-deep: #0054AA;
    --brand-mid: #0677BA;
    --brand-bright: #0094D4;
    --ink: #3a3a3c;
    --ink-soft: #4a4a4c;
  }
  html, body {
    margin: 0;
    width: 942px;
    height: 1200px;
    overflow: hidden;
    background: var(--backdrop);
  }
  .letterhead {
    position: absolute;
    left: 45px;
    top: 0;
    width: 851px;
    height: 1200px;
    background: var(--paper);
    font-family: "Arimo", Arial, sans-serif;
    color: var(--ink);
  }
  .brand {
    position: absolute;
    left: 57px;
    top: 92px;
    display: flex;
    align-items: center;
    gap: 10px;
  }
  .brand-dot {
    width: 34px;
    height: 34px;
    border-radius: 50%;
    background: var(--brand-bright);
    flex: none;
  }
  .brand-name {
    font-family: "Arimo", Arial, sans-serif;
    font-weight: 600;
    font-size: 17px;
    line-height: 20px;
    color: var(--brand-deep);
    width: 130px;
  }
  .contact {
    position: absolute;
    left: 553px;
    top: 76px;
    font-family: "Open Sans", Arial, sans-serif;
    font-size: 13.2px;
    color: #2b2b2d;
  }
  .contact-address {
    margin: 0 0 8px;
    line-height: 18px;
    text-transform: uppercase;
  }
  .contact-address span { text-transform: none; }
  .contact-list { list-style: none; margin: 0; padding: 0; }
  .contact-list li {
    display: flex;
    align-items: center;
    gap: 7px;
    line-height: 18px;
  }
  .contact-list svg { width: 12px; height: 12px; fill: var(--brand-mid); flex: none; }
  .letter {
    position: absolute;
    left: 59px;
    top: 296px;
    width: 735px;
  }
  .salutation {
    font-size: 24px;
    font-weight: 400;
    margin: 0 0 40px;
    color: var(--ink-soft);
  }
  .letter-body p {
    font-size: 13.3px;
    line-height: 17.6px;
    text-align: justify;
    margin: 0 0 22px;
    letter-spacing: -0.05px;
  }
  .closing { font-size: 13.3px; margin: 27px 0 0; }
  .signature {
    position: absolute;
    left: 68px;
    top: 874px;
    width: 110px;
    height: 44px;
    background: linear-gradient(90deg, rgba(40,44,60,0.18), rgba(40,44,60,0.08));
    border-radius: 4px;
  }
  .signatory {
    position: absolute;
    left: 69px;
    top: 938px;
  }
  .signatory-name { font-size: 18px; margin: 0; color: var(--ink-soft); }
  .signatory-role { font-size: 14.5px; margin: 6px 0 0; color: var(--ink-soft); }
</style>
</head>
<body>
  <main class="letterhead">
    <header>
      <div class="brand">
        <span class="brand-dot"></span>
        <span class="brand-name">All Sorted Property Services</span>
      </div>
      <address class="contact" style="font-style:normal">
        <p class="contact-address">14 Harbour Lane Palm Cove<br>Queensland, 4870 <span>Australia</span></p>
        <ul class="contact-list">
          <li><svg viewBox="0 0 24 24"><path d="M6.6 10.8a15.2 15.2 0 0 0 6.6 6.6l2.2-2.2a1 1 0 0 1 1-.25 11.4 11.4 0 0 0 3.6.57 1 1 0 0 1 1 1V20a1 1 0 0 1-1 1A17 17 0 0 1 3 4a1 1 0 0 1 1-1h3.5a1 1 0 0 1 1 1c0 1.25.2 2.45.57 3.57a1 1 0 0 1-.25 1z"/></svg>555-010-2468</li>
          <li><svg viewBox="0 0 24 24"><path d="M2 5h20v14H2z M2 5l10 8 10-8" fill="none" stroke="#0677BA" stroke-width="0"/><path d="M2 6l10 7 10-7V5H2zm0 2.4V19h20V8.4l-10 7z"/></svg>info@allsortedproperty.com.au</li>
          <li><svg viewBox="0 0 24 24"><circle cx="12" cy="12" r="10"/></svg>www.allsortedproperty.com.au</li>
        </ul>
      </address>
    </header>

    <section class="letter">
      <h1 class="salutation">Dear Mr. Carter,</h1>
      <div class="letter-body">
        <p>Lorem ipsum dolor sit amet, consectetur adipiscing elit. Donec orci purus, luctus vitae dignissim eu, iaculis sed purus. Vivamus faucibus, ipsum nec aliquet viverra, leo mauris condimentum ligula, sit amet sagittis enim ligula quis arcu. Nam egestas tortor id nisi porttitor mattis. In tortor ante, ultricies in suscipit a, tempus non massa. Vivamus et auctor mi. Fusce vel massa nulla. Phasellus nec eros mauris, et scelerisque orci.</p>
        <p>Donec malesuada orci vitae nulla accumsan porta a id massa. Quisque accumsan iaculis magna sit amet fringilla. Maecenas consequat, magna eget tincidunt semper, odio nibh rutrum mi, id feugiat ante nisi eu risus. Vestibulum nunc orci, rhoncus a placerat in, ultricies in mi. Cras mattis varius eros, vel fringilla nisi suscipit eget. Quisque scelerisque sagittis nulla at porttitor.</p>
        <p>Sed id augue vitae urna euismod commodo aliquet a quam. Pellentesque arcu velit, cursus et malesuada ut, consequat et diam. Nullam erat sem, rhoncus id ullamcorper vitae, rhoncus et arcu. In ultricies ultricies nulla, ut rutrum nisi iaculis at. Donec eu magna a metus ornare faucibus. Fusce aliquet faucibus ultricies. Morbi semper, est id tincidunt gravida, sem arcu adipiscing lacus, ac bibendum nulla leo eu purus. Quisque nec diam sed risus consectetur a ccumsan quis quis nibh. Vestibulum id purus lorem.</p>
        <p>It is a long established fact that a reader will be distracted by the readable content of a page when looking at its layout. The point of using Lorem Ipsum is that it has a more-or-less normal distribution of letters, as opposed to using ‘Content here, content here’, making it look like readable English. Many desktop publishing packages</p>
        <p class="closing">Sincerely,</p>
      </div>
    </section>

    <div class="signature" role="img" aria-label="Handwritten signature of James Carter"></div>
    <footer class="signatory">
      <p class="signatory-name">James Carter</p>
      <p class="signatory-role">CEO/ Founder</p>
    </footer>
  </main>
</body>
</html>
```